Healthy Vending Machine Business Flyer

A modorn design that represents our healthy vending machine business. We will attach a picture of the machine we want on the flyer along with our logo. We will also upload the wording we want on the flyer

Colors

Designer to choose colors to be used in the design.

Requirements
Must have
• Flyer wording
• Front of flyer:
• (Picture of vending machine on the front)
• Free healthy vending machines hit the Treasure Valley
• Keep your Employees happy & productive with healthy vending options at work
• • No Cost to Your Company
• • Remote tracking tells us when your favorite snacks are running low
• • Credit Card/Smartphone Payment Technology
• • Ability to Customize your Snacks and Drinks
• • Locally Owned and Operated
• • Delicious Healthy Options
• Back of flyer:
• Quillow Healthy Vending is a locally owned and operated company dedicated to making healthy snacks and drinks easily available for the Treasure Valley. We provide the latest in vending machine technology accepting credit cards, zenno pay, and nimbus wallet. State of the art inventory tracking tells us when your machine is running low so you're never out of your favorite drink or snack. We offer flexible stocking based on your companies needs and work with you on what items you want in the machine. Our goal is to give your employees and clients healthy options on the go
• To be considered for this FREE service for your business please visit: quillowhealthyvending.com
• Or call/email today:
• Phone: 555-201-4736
• Email: quillowhealthyvending@mailvex.com
Should not have
• Any Additional Fruit images besides what is on the machine image.

```html
<!DOCTYPE html>
<html lang="en">
<head>
<meta charset="UTF-8">
<title>Quillow Healthy Vending Flyer</title>
<link rel="stylesheet" href="https://fonts.googleapis.com/css2?family=Montserrat:wght@500;600;700&display=swap">
<style>
:root{
  --green:#3f8e00;
  --orange:#f07800;
  --orange-deep:#e0620a;
  --white:#ffffff;
  --ink:#333333;
  --stage:#9c9c9c;
}
*{margin:0;padding:0;box-sizing:border-box}
html,body{width:1200px;height:894px;overflow:hidden}
body{background:radial-gradient(ellipse at center,#c4c4c4 0%,var(--stage) 75%);font-family:"Montserrat",sans-serif;position:relative}
.page{position:absolute;top:73px;width:539px;height:746px;overflow:hidden;box-shadow:0 6px 14px rgba(0,0,0,.35)}
.front{left:51px;background:var(--green)}
.back{left:606px;width:532px;background:var(--white)}

.brand{position:absolute;left:0;right:0;display:flex;align-items:center;justify-content:center;gap:10px;font-weight:700;font-size:32px;letter-spacing:-.3px}
.brand-dot{width:18px;height:18px;border-radius:50%;flex:none}
.front .brand{top:88px;color:var(--white)}
.front .brand-dot{background:var(--white)}
.back .brand{top:110px;color:var(--orange)}
.back .brand-dot{background:var(--orange)}

.headline{position:absolute;top:178px;left:0;right:0;text-align:center;color:var(--white);font-weight:700;font-size:22.5px;line-height:27px;letter-spacing:.3px;text-transform:uppercase}
.intro{position:absolute;top:245px;left:26px;width:482px;color:var(--white);font-weight:700;font-size:17px;line-height:23px;text-align:justify;text-align-last:left;word-spacing:4px}

.benefits{position:absolute;top:310px;left:23px;width:245px;list-style:none;color:var(--white);font-weight:500;font-size:14px;line-height:19px}
.benefits li{position:relative;padding-left:27px;text-align:justify;text-align-last:left;word-spacing:2px}
.benefits li svg{position:absolute;left:0;top:3px;width:17px;height:17px}

.machine{position:absolute;left:287px;top:294px;width:223px;height:400px;background:linear-gradient(100deg,#1c1c1c 0%,#2a2a2a 45%,#7a9a2a 60%,#c0321e 80%,#d85a20 100%);clip-path:polygon(2% 9%,12% 4%,55% 0,100% 5%,100% 88%,55% 100%,3% 90%)}

.swoosh{position:absolute;left:0;top:560px;width:539px;height:186px}
.leaf-mark{position:absolute;left:124px;top:582px;width:58px;height:45px;background:radial-gradient(circle at 50% 40%,var(--orange) 0%,#f39440 70%,transparent 71%)}
.front-url{position:absolute;left:0;right:0;top:700px;text-align:center;color:var(--orange);font-weight:700;font-size:24.5px;letter-spacing:.2px}

.about{position:absolute;top:225px;left:41px;width:447px;color:var(--ink);font-weight:500;font-size:17.4px;line-height:24.5px;text-align:justify;text-align-last:center}

.contact-band{position:absolute;left:0;right:0;top:599px;bottom:0;background:var(--green)}
.phone{position:absolute;left:112px;top:568px;width:309px;height:64px;border-radius:32px;background:var(--orange-deep);border:4px solid var(--white);display:flex;align-items:center;justify-content:center;color:var(--white);font-weight:700;font-size:32px;letter-spacing:.5px}
.cta{position:absolute;top:646px;left:0;right:0;text-align:center;color:var(--white);font-weight:700;font-size:19.6px;line-height:26px;text-transform:uppercase}
.links{position:absolute;top:704px;left:0;right:0;display:flex;justify-content:center;gap:18px;color:var(--white);font-weight:600;font-size:11px;text-transform:uppercase}
.links span{display:flex;align-items:center;gap:6px}
.links svg{width:19px;height:19px}
</style>
</head>
<body>

<section class="page front">
  <div class="brand"><span class="brand-dot"></span>Quillow Healthy Vending</div>

  <h1 class="headline">Free Healthy Vending<br>Machines Hit the Treasure Valley</h1>
  <p class="intro">Keep your Employees happy &amp; productive with healthy vending options at work</p>

  <ul class="benefits">
    <li style="margin-top:0"><svg viewBox="0 0 20 20"><circle cx="10" cy="10" r="8" fill="none" stroke="#fff" stroke-width="1.8" stroke-dasharray="40 8"/><path d="M6 10l3 3 7-8" fill="none" stroke="#fff" stroke-width="2"/></svg>No Cost to Your Company</li>
    <li style="margin-top:15px"><svg viewBox="0 0 20 20"><circle cx="10" cy="10" r="8" fill="none" stroke="#fff" stroke-width="1.8" stroke-dasharray="40 8"/><path d="M6 10l3 3 7-8" fill="none" stroke="#fff" stroke-width="2"/></svg>Remote tracking tells us when your favorite snacks are running low</li>
    <li style="margin-top:12px"><svg viewBox="0 0 20 20"><circle cx="10" cy="10" r="8" fill="none" stroke="#fff" stroke-width="1.8" stroke-dasharray="40 8"/><path d="M6 10l3 3 7-8" fill="none" stroke="#fff" stroke-width="2"/></svg>Credit Card/Smartphone Payment Technology</li>
    <li style="margin-top:17px"><svg viewBox="0 0 20 20"><circle cx="10" cy="10" r="8" fill="none" stroke="#fff" stroke-width="1.8" stroke-dasharray="40 8"/><path d="M6 10l3 3 7-8" fill="none" stroke="#fff" stroke-width="2"/></svg>Ability to Customize your Snacks and Drinks</li>
    <li style="margin-top:14px"><svg viewBox="0 0 20 20"><circle cx="10" cy="10" r="8" fill="none" stroke="#fff" stroke-width="1.8" stroke-dasharray="40 8"/><path d="M6 10l3 3 7-8" fill="none" stroke="#fff" stroke-width="2"/></svg>Locally Owned and Operated</li>
    <li style="margin-top:13px"><svg viewBox="0 0 20 20"><circle cx="10" cy="10" r="8" fill="none" stroke="#fff" stroke-width="1.8" stroke-dasharray="40 8"/><path d="M6 10l3 3 7-8" fill="none" stroke="#fff" stroke-width="2"/></svg>Delicious Healthy Options</li>
  </ul>

  <svg class="swoosh" viewBox="0 0 539 186" preserveAspectRatio="none">
    <path d="M0 46 Q260 110 539 30 L539 186 L0 186 Z" fill="#ffffff"/>
    <path d="M0 52 Q250 128 539 46" fill="none" stroke="#f07800" stroke-width="5"/>
  </svg>
  <div class="leaf-mark" role="img" aria-label="Small orange leaf ornament"></div>

  <div class="machine" role="img" aria-label="Photo of a healthy snack and drink vending machine wrapped in fruit graphics"></div>

  <p class="front-url">QUILLOWHEALTHYVENDING.COM</p>
</section>

<section class="page back">
  <div class="brand"><span class="brand-dot"></span>Quillow Healthy Vending</div>

  <p class="about">Quillow Healthy Vending is a locally owned and operated company dedicated to making healthy snacks and drinks easily available for the Treasure Valley. We provide the latest in vending machine technology accepting credit cards, zenno pay, and nimbus wallet. State of the art inventory tracking tells us when your machine is running low so you're never out of your favorite drink or snack. We offer flexible stocking based on your companies needs and work with you on what items you want in the machine. Our goal is to give your employees and clients healthy options on the go.</p>

  <div class="contact-band"></div>
  <div class="phone">555-201-4736</div>
  <p class="cta">To be considered for this free service<br>for your business please visit:</p>
  <div class="links">
    <span><svg viewBox="0 0 20 20" fill="none" stroke="#fff" stroke-width="1.3"><circle cx="10" cy="10" r="8.5"/><ellipse cx="10" cy="10" rx="3.8" ry="8.5"/><path d="M1.5 10h17M3 5.5h14M3 14.5h14"/></svg>quillowhealthyvending.com</span>
    <span><svg viewBox="0 0 20 20" fill="none" stroke="#fff" stroke-width="1.3"><rect x="1.5" y="4.5" width="17" height="11" fill="#fff"/><path d="M1.5 4.5l8.5 6.5 8.5-6.5M1.5 15.5l6-5.5M18.5 15.5l-6-5.5" stroke="#3f8e00"/></svg>quillowhealthyvending@mailvex.com</span>
  </div>
</section>

</body>
</html>
```